Design of retail home garden product

We are searching for a modern and out of the box but practical design for our home garden product. The example product is called mossvanish and removes green pollution on walls, buildings, and pavements.
We would like a futuristic design that we can use for our whole product line home garden, which should emphasize the future, eco, bright colors, modern shapes, clear images and an appealing look for the retail market. Currently we have three products in our home garden line, a green pollution remover, nanotechnology spray for masks and a natural bug cleaner.

Target Market(s)

Retail

Industry/Entity Type

Retail

Font styles to use
Sans Serif

Requirements
Must have
• Modern design, retail design, see in 1 look what the product does, home garden look and feel
Nice to have
• Icons, practical items that shows what the product does, modern logo design
Should not have
• Outdated design

```html
<!DOCTYPE html>
<html lang="nl">
<head>
<meta charset="utf-8">
<title>mossvanish – product label</title>
<link rel="stylesheet" href="https://fonts.googleapis.com/css2?family=Raleway:wght@200;800&family=Poppins:wght@700&family=Roboto+Condensed:wght@400;700&display=swap">
<style>
  :root {
    --white: #ffffff;
    --teal: #18b2bd;
    --teal-mid: #1c9aa4;
    --teal-dark: #0d5f68;
    --teal-light: #7fd3d3;
    --yellow: #f6d21e;
    --leaf-green: #45a83a;
    --orange: #f0821e;
    --panel-red: #ea5359;
    --pink-2: #f5b3b1;
    --pink-3: #ef8a8b;
    --ink: #ffffff;
    --ink-dark: #2a1416;
  }
  html, body { margin: 0; padding: 0; overflow: hidden; background: var(--white); }
  .label {
    position: relative;
    width: 1200px;
    height: 810px;
    overflow: hidden;
    background: var(--white);
    font-family: "Raleway", sans-serif;
  }
  .front-shapes { position: absolute; left: 0; top: 0; width: 734px; height: 810px; }

  .brand-name {
    position: absolute; left: 396px; top: 60px; width: 264px; height: 198px;
    display: flex; align-items: center; justify-content: center; gap: 12px;
  }
  .brand-name__dot {
    width: 22px; height: 22px; border-radius: 50%; background: var(--leaf-green);
  }
  .brand-name__text {
    font-family: "Raleway", sans-serif; font-weight: 800;
    color: var(--leaf-green); font-size: 50px; line-height: 1;
  }

  .product-name { margin: 0; position: absolute; left: 0; top: 0; }
  .product-name__first {
    position: absolute; left: 146px; top: 340px;
    font-family: "Raleway", sans-serif; font-weight: 200;
    font-size: 150px; color: var(--teal); line-height: 1; white-space: nowrap;
  }
  .product-name__banner { position: absolute; left: 0; top: 0; width: 734px; height: 810px; }
  .product-name__second {
    position: absolute; left: 160px; top: 486px;
    font-family: "Poppins", sans-serif; font-weight: 700;
    font-size: 124px; color: var(--teal); line-height: 1; white-space: nowrap;
    letter-spacing: -2px;
  }
  .web-address {
    position: absolute; left: 48px; top: 706px;
    font-family: "Raleway", sans-serif; font-weight: 800;
    font-size: 24px; color: var(--orange);
  }

  .info-panel {
    position: absolute; left: 734px; top: 0; width: 466px; height: 810px;
    background: var(--panel-red);
    font-family: "Roboto Condensed", sans-serif;
    color: var(--ink); font-size: 11.8px; line-height: 15px;
  }
  .hazard-icon { position: absolute; left: 30px; top: 40px; width: 36px; height: 36px; }
  .info-panel p { margin: 0; position: absolute; left: 94px; width: 328px; }
  .info-panel strong { font-weight: 700; }
  .usage-rules { top: 32px; text-align: justify; }
  .usage-directions { top: 186px; text-align: justify; }
  .maker { top: 308px; }
  .batch { top: 378px; color: var(--ink-dark); font-weight: 700; white-space: nowrap; letter-spacing: -0.1px; }
  .code { top: 404px; }
  .warnings { top: 446px; text-align: justify; }
  .pet-notice { top: 630px; }
  .registration { top: 752px; font-weight: 700; padding-left: 4px; }
</style>
</head>
<body>
<main class="label">

  <svg class="front-shapes" viewBox="0 0 734 810" aria-hidden="true">
    <defs>
      <linearGradient id="tealDepth" x1="0" y1="0" x2="1" y2="1">
        <stop offset="0" stop-color="#0a4e56"/>
        <stop offset="1" stop-color="#168c95"/>
      </linearGradient>
      <linearGradient id="pinkFade" x1="0" y1="1" x2="1" y2="0">
        <stop offset="0" stop-color="#fde8e6"/>
        <stop offset="1" stop-color="#f3a9a8"/>
      </linearGradient>
    </defs>
    <path d="M0,0 H345 C310,170 200,300 0,420 Z" fill="var(--teal-light)"/>
    <path d="M0,0 H310 C270,150 170,260 0,365 Z" fill="var(--teal-mid)"/>
    <path d="M0,0 H255 C215,130 130,215 0,295 Z" fill="url(#tealDepth)"/>
    <path d="M0,0 H150 C120,80 70,130 0,170 Z" fill="var(--teal-dark)" opacity="0.8"/>

    <path d="M140,810 C330,650 540,500 734,400 V810 Z" fill="url(#pinkFade)"/>
    <path d="M330,810 C470,700 610,630 734,600 V810 Z" fill="var(--pink-2)"/>
    <path d="M420,810 C540,730 640,690 734,680 V810 Z" fill="var(--white)" opacity="0.45"/>
    <path d="M560,810 C620,760 690,738 734,732 V810 Z" fill="var(--pink-3)"/>
  </svg>

  <div class="brand-name">
    <span class="brand-name__dot"></span>
    <span class="brand-name__text">lindehof</span>
  </div>

  <h1 class="product-name">
    <span class="product-name__first">Moss</span>
    <svg class="product-name__banner" viewBox="0 0 734 810" aria-hidden="true">
      <polygon points="132,542 690,548 648,630 130,632" fill="var(--yellow)"/>
    </svg>
    <span class="product-name__second">vanish</span>
  </h1>

  <div class="web-address">lindehofchemicals.com</div>

  <section class="info-panel">
    <svg class="hazard-icon" viewBox="0 0 40 40" aria-label="Gevarensymbool">
      <rect x="8" y="8" width="24" height="24" transform="rotate(45 20 20)" fill="#fff" stroke="#d3171f" stroke-width="3"/>
      <rect x="18.3" y="11" width="3.4" height="12" rx="1" fill="#111"/>
      <circle cx="20" cy="27.5" r="2" fill="#111"/>
    </svg>

    <p class="usage-rules"><strong>Wettelijk gebruiksvoorschrift:</strong><br>
    Toegestaan is uitsluitend het gebruik als middel ter bestrijding van groene aanslag. Het behandelen van verharde oppervlakken en apparatuur naast watergangen bij de bestrijding van groene aanslag is niet toegestaan. Dit middel is giftig voor vissen en andere waterorganismen. Voorkomen moet worden dat de vloeistof het oppervlaktewater bereikt.</p>

    <p class="usage-directions"><strong>Gebruiksaanwijzing:</strong><br>
    Ter verwijdering en ter voorkoming van groene aanslag op muren, daken, tegelpaden, flagstones, grafzerken, ramen, bielsen, tuinmeubelen e.d. Spuiten, gieten, borstelen of schrobben met een oplossing van<br>
    2,5% van dit middel (25 ml op 1 liter water). Niet naspoelen.<br>
    Niet op planten spuiten of gieten.</p>

    <p class="maker">LINDEHOF LABORATORIES int. B.V.<br>
    Postbus 20417 5900 AB Venlo (NL)<br>
    +31 477 20 19 00<br>
    WWW.LINDEHOFLABS.COM</p>
    <p class="batch">Chargenummer: zie verpakking.&nbsp; Netto volume: zie verpakking.</p>

    <p class="code">070520</p>

    <p class="warnings">Gevaar: Veroorzaakt ernstige brandwonden en oogletsel, Zeer giftig voor in het water levende organismen, met langdurige gevolgen.Voorkom lozing in het milieu. Beschermende handschoenen, beschermende kleding, oogbescherming, gelaatsbescherming dragen. NA INSLIKKEN: de mond spoelen — GEEN braken opwekken. BIJ CONTACT MET DE OGEN: voorzichtig afspoelen met water gedurende een aantal minuten; contactlenzen verwijderen, indien mogelijk; blijven spoelen. Onmiddellijk een ANTIGIFCENTRUM of een arts raadplegen. Didecyldimethylammoniumchloride</p>

    <p class="pet-notice">Houd huisdieren weg van de behandelde plekken, zolang deze nog vochtig zijn.<br>
    <strong>Opmerking:</strong> Het middel wordt onwerkzaam wanneer het in contact komt met zeep of synthetische wasmiddelen. <strong>Aard van het preparaat:</strong> vloeistof<br>
    Werkzame stof(fen): didecyldimethylammoniumchloride.<br>
    Gehalte: 100 g/l. Andere zeer giftige, giftige, bijtende of schadelijke stof(fen): ---</p>

    <p class="registration">Toelatingsnummer: 13123 N</p>
  </section>

</main>
</body>
</html>
```